Capability statement for an Electrical Business based in Sydney Australia

The aim for the Capability statement is for us to look more professional when we meet someone or after cold calling and have to send them our business details.
Need something simple, efficient and to the point.

It should have the following content
- Our mission (details can be as attached PDF)
- Areas we service (this can be a google map of areas we service but basically the areas are
Metro Sydney with our work centralised around the Norwest, Hills, Inner west and Epping area)
- List of services we provide (as PDF)
- Details about us; who we are, contact details, licenses (as PDF)
- Why they should choose us
(As pdf)

Right now, we're just after a nice format we're happy with, the details we are happy to provide with once we have a design in mind.

I've attached our current existing capability statement and what our details are. Also, our website is
https://brightwirepro.com.au/

Thanks in advance!

Requirements
Should not have
• Should not be complicated for the reader

```html
<!DOCTYPE html>
<html lang="en">
<head>
<meta charset="utf-8">
<title>BrightWire Pro – Capability Statement</title>
<link rel="stylesheet" href="https://fonts.googleapis.com/css2?family=Oswald:wght@500;600&family=Poppins:wght@400;500;600;700;800&family=Russo+One&display=swap">
<style>
:root{
  --red:#e8261e;
  --red-dark:#c81912;
  --ink:#151515;
  --charcoal:#2b2828;
  --panel:#1b1919;
  --grey-tag:#e3dede;
  --muted:#3c3c3c;
  --white:#ffffff;
  --backdrop:#eceeef;
  --photo-a:#8d8074;
  --photo-b:#4a4540;
}
*{box-sizing:border-box;margin:0;padding:0}
html,body{width:815px;height:1200px;overflow:hidden}
body{background:var(--backdrop);font-family:"Poppins",sans-serif;color:var(--ink);position:relative}

.page{position:absolute;left:187px;width:440px;height:571px;background:var(--white);overflow:hidden;box-shadow:0 6px 22px rgba(0,0,0,.14)}
.page--front{top:18px}
.page--back{top:611px}
.abs{position:absolute}

/* brand */
.brand{position:absolute;left:26px;top:32px;display:flex;align-items:center;gap:5px}
.brand__mark{width:10px;height:10px;background:var(--red)}
.brand__name{font-family:"Poppins",sans-serif;font-weight:800;font-size:15.5px;letter-spacing:.2px;color:var(--red);line-height:1;white-space:nowrap}

/* photo placeholders */
.photo{position:absolute;background:linear-gradient(135deg,var(--photo-a),var(--photo-b))}

/* ---------- front ---------- */
.front__dark{left:308px;top:0;width:132px;height:258px;background:var(--charcoal)}
.front__photo{left:226px;top:24px;width:190px;height:206px;border-radius:14px 40px 14px 40px;border:3px solid var(--white)}
.front__kicker{left:26px;top:80px;font-family:"Russo One",sans-serif;font-size:19px;color:var(--ink);letter-spacing:.3px}
.front__title{left:24px;top:100px;font-family:"Oswald",sans-serif;font-weight:600;font-size:42px;line-height:40px;color:var(--red);letter-spacing:-.5px}
.front__intro{left:40px;top:193px;width:176px;font-size:10px;line-height:12.6px;color:var(--ink)}
.front__intro-bar{left:26px;top:196px;width:3px;height:44px;background:var(--red)}

.who{left:0;top:251px;width:440px;height:64px;background:linear-gradient(90deg,var(--red) 0%,var(--red-dark) 60%,var(--red) 100%);color:var(--white);padding:5px 26px 0}
.who__title{font-weight:700;font-size:9.5px;color:var(--ink);letter-spacing:.2px}
.who__text{font-size:6.2px;line-height:8.4px;margin-top:2px}

.cap-title{left:0;top:321px;width:440px;text-align:center;font-weight:700;font-size:14px;letter-spacing:.2px}
.cap-title span{color:var(--red)}

.mission{left:26px;top:342px;display:flex;align-items:center;gap:6px}
.mission__label{font-family:"Oswald",sans-serif;font-weight:600;font-size:16px;letter-spacing:.2px}
.mission__divider{width:1px;height:16px;background:var(--ink)}
.mission__text{font-size:8px;line-height:10px;width:270px}

.dotline{left:26px;top:375px;width:388px;border-top:1px dashed #888}

.core{left:26px;top:397px;font-family:"Russo One",sans-serif;font-size:17px;line-height:15px}
.core small{display:block;font-family:"Poppins",sans-serif;font-weight:500;font-size:14px;line-height:15px}
.value{position:absolute;top:398px;width:62px;height:46px;border:1.4px solid var(--ink);border-radius:6px;text-align:center;font-size:6px;line-height:7.2px;padding:13px 5px 0}
.value__icon{position:absolute;left:50%;top:-12px;transform:translateX(-50%);width:22px;height:22px;border-radius:50%;background:var(--white);border:1.4px solid var(--red);display:flex;align-items:center;justify-content:center}
.value__icon i{width:16px;height:16px;border-radius:50%;background:var(--red);display:flex;align-items:center;justify-content:center}
.value--alt .value__icon{border-color:var(--ink)}
.value--alt .value__icon i{background:var(--ink)}
.value-arrow{position:absolute;top:418px;width:22px;height:10px}

.services{left:0;top:457px;width:440px;height:114px;background:var(--panel);color:var(--white)}
.services__title{position:absolute;left:0;top:7px;width:440px;text-align:center;font-family:"Oswald",sans-serif;font-weight:500;font-size:12.5px;color:var(--red);letter-spacing:.1px}
.services__col{position:absolute;top:29px;list-style:none;font-size:5.6px;line-height:6.6px}
.services__col li{position:relative;padding-left:8px;margin-bottom:5px}
.services__col li::before{content:"";position:absolute;left:0;top:1px;width:4px;height:4px;background:var(--red);border-radius:1px}
.services__sep{position:absolute;top:30px;height:66px;border-left:1px dashed #bbb}

/* ---------- back ---------- */
.back__dark{left:314px;top:0;width:126px;height:189px;background:var(--charcoal)}
.back__photo{left:200px;top:13px;width:224px;height:154px;border-radius:36px;border:3px solid var(--red)}
.why{left:26px;top:78px;font-family:"Russo One",sans-serif;font-size:32px;line-height:33px;color:var(--ink)}
.why span{color:var(--red)}
.why__brand{left:26px;top:148px;font-weight:700;font-size:16px;color:var(--red);letter-spacing:.2px}
.why__rule{left:26px;top:174px;width:165px;height:1.5px;background:var(--red)}
.why__rule::before{content:"";position:absolute;left:8px;top:-1px;width:36px;height:3.5px;background:var(--ink);border-radius:2px}

.feature{position:absolute;width:182px}
.feature__head{display:flex;align-items:center;height:30px}
.feature__icon{width:30px;height:30px;background:var(--red);display:flex;align-items:center;justify-content:center;clip-path:polygon(0 0,100% 0,100% 70%,75% 100%,0 100%)}
.feature__label{flex:1;height:24px;margin-left:-2px;background:var(--grey-tag);clip-path:polygon(0 0,94% 0,100% 50%,94% 100%,0 100%);padding-left:16px;font-weight:600;font-size:8.6px;line-height:10px;display:flex;align-items:center}
.feature__text{margin-top:16px;font-size:6.6px;line-height:8.6px;color:var(--ink)}

.contact-title{left:26px;top:396px;font-weight:700;font-size:15px;line-height:17px;letter-spacing:.3px}
.contact-title span{color:var(--red)}
.contact-rule{left:26px;top:438px;width:165px;height:1.5px;background:var(--red)}
.person{position:absolute;top:448px}
.person__name{font-weight:700;font-size:7.6px;line-height:9px}
.person__name--red{color:var(--red)}
.pill{display:flex;align-items:center;gap:3px;margin-top:1px;height:13px;padding:0 5px 0 2px;border-radius:3px;font-weight:700;font-size:8px;color:var(--white)}
.pill--ink{background:var(--ink)}
.pill--red{background:var(--red)}
.pill__dot{width:9px;height:9px;border-radius:50%;background:var(--white);display:flex;align-items:center;justify-content:center}
.lic{left:26px;top:485px;font-size:6.8px;line-height:8.2px;font-weight:700}
.lic span{color:var(--red);display:block}
.liability{left:26px;top:510px;font-weight:700;font-size:12px;line-height:12.5px}
.liability span{color:var(--red);display:block}

.badge{position:absolute;top:474px;width:72px}
.badge__name{border:1.4px solid var(--red);border-bottom:none;border-radius:3px 3px 0 0;text-align:center;font-weight:700;font-size:8px;line-height:9px;color:var(--red);background:var(--white)}
.badge__num{display:flex;align-items:center;gap:4px;background:var(--ink);color:var(--white);font-weight:700;font-size:8.5px;line-height:12px;padding:0 4px;border-radius:0 0 3px 3px}
.badge__num i{width:7px;height:7px;background:var(--red);border-radius:1px}
.abn{left:233px;top:507px;font-weight:700;font-size:7px}

.email{left:202px;top:528px;width:238px;height:20px;background:var(--ink);border-radius:10px 0 0 10px;color:var(--white);font-size:9px;display:flex;align-items:center;padding-left:12px;gap:6px}
.back__foot{left:0;top:561px;width:440px;height:10px;background:var(--ink)}
</style>
</head>
<body>

<!-- Front page -->
<section class="page page--front" aria-label="Capability statement front">
  <div class="abs front__dark"></div>
  <div class="photo front__photo" role="img" aria-label="Photo of a modern living room with pendant lights, sofa and timber floor"></div>

  <div class="brand"><span class="brand__mark"></span><span class="brand__name">BRIGHTWIRE PRO</span></div>

  <div class="abs front__kicker">SYDNEY BASED</div>
  <h1 class="abs front__title">ELECTRICAL<br>BUSINESS</h1>
  <div class="abs front__intro-bar"></div>
  <p class="abs front__intro">specialising in electrical mainte-nance work for residential, com-mercial, strata and real estate clients.</p>

  <div class="abs who">
    <h2 class="who__title">WHO WE ARE</h2>
    <p class="who__text">BrightWire Pro is a growing Electrical maintenance company based in the Inner West. We are established on sound service principles with honesty, communication, and respect at the forefront of every team member. We strive for openness, trust, and accountability and we are in the business of providing solu-tions to help others. We see ourselves as an extension of your team.</p>
  </div>

  <h2 class="abs cap-title"><span>CAPABILITY</span> STATEMENT</h2>

  <div class="abs mission">
    <svg width="15" height="15" viewBox="0 0 16 16" aria-hidden="true"><circle cx="8" cy="8" r="6.5" fill="none" stroke="#e8261e" stroke-width="2"/><circle cx="8" cy="8" r="3" fill="none" stroke="#e8261e" stroke-width="1.6"/><path d="M8 8 L15 1" stroke="#151515" stroke-width="1.6"/></svg>
    <span class="mission__label">MISSION</span>
    <span class="mission__divider"></span>
    <p class="mission__text">Dedicate ourselves to providing world class service to anyone in need, based on honesty, communication and respect.</p>
  </div>

  <div class="abs dotline"></div>

  <div class="abs core">CORE<small>VALUES</small></div>

  <div class="value" style="left:101px"><span class="value__icon"><i><svg width="9" height="9" viewBox="0 0 10 10"><path d="M5 .5 9 2v3c0 2.3-1.7 3.8-4 4.5C2.7 8.8 1 7.3 1 5V2z" fill="#fff"/></svg></i></span>Safety and Security is priority</div>
  <svg class="value-arrow" style="left:162px" viewBox="0 0 22 10" aria-hidden="true"><path d="M0 2h6v6h14M17 5l3 3-3 3" fill="none" stroke="#e8261e" stroke-width="1.3"/></svg>
  <div class="value value--alt" style="left:184px"><span class="value__icon"><i><svg width="9" height="9" viewBox="0 0 10 10"><path d="M1.5 6V5a3.5 3.5 0 0 1 7 0v1" fill="none" stroke="#fff" stroke-width="1.3"/><rect x="1" y="5.5" width="2" height="3" fill="#fff"/><rect x="7" y="5.5" width="2" height="3" fill="#fff"/></svg></i></span>Support when you need it most</div>
  <svg class="value-arrow" style="left:245px" viewBox="0 0 22 10" aria-hidden="true"><path d="M0 2h6v6h14M17 5l3 3-3 3" fill="none" stroke="#151515" stroke-width="1.3"/></svg>
  <div class="value" style="left:267px"><span class="value__icon"><i><svg width="9" height="9" viewBox="0 0 10 10"><circle cx="5" cy="5" r="2.2" fill="none" stroke="#fff" stroke-width="1.4"/><circle cx="5" cy="5" r="4" fill="none" stroke="#fff" stroke-width="1" stroke-dasharray="1.6 1.2"/></svg></i></span>Service with an over-the-top WOW</div>
  <svg class="value-arrow" style="left:328px" viewBox="0 0 22 10" aria-hidden="true"><path d="M0 2h6v6h14M17 5l3 3-3 3" fill="none" stroke="#e8261e" stroke-width="1.3"/></svg>
  <div class="value value--alt" style="left:350px"><span class="value__icon"><i><svg width="9" height="9" viewBox="0 0 10 10"><path d="M5 1l1.1 2.3 2.5.3-1.8 1.7.5 2.5L5 6.6 2.7 7.8l.5-2.5L1.4 3.6l2.5-.3z" fill="#fff"/></svg></i></span>Satisfaction with loyalty and integrity</div>

  <div class="abs services">
    <h2 class="services__title">BRIEF LIST OF THE MOST COMMON SERVICES WE PROVIDE</h2>
    <ul class="services__col" style="left:26px;width:106px">
      <li>24/7 Emergency service</li>
      <li>Switchboard UPGRADE and REPAIRS</li>
      <li>Light fitting installations</li>
      <li>Powerpoint installations</li>
    </ul>
    <span class="services__sep" style="left:136px"></span>
    <ul class="services__col" style="left:146px;width:124px">
      <li>Surge device installations</li>
      <li>Testing and servicing electric hot water systems</li>
      <li>Smoke Alarm installation with compliance certificate</li>
      <li>Electric Vehicle charging stations</li>
    </ul>
    <span class="services__sep" style="left:275px"></span>
    <ul class="services__col" style="left:285px;width:132px">
      <li>Ceiling and Exhaust fan installations with roof and wall venting</li>
      <li>Appliance installations</li>
      <li>Fault finding</li>
      <li>TV, DATA and FREE TO AIR Aerial installations</li>
    </ul>
  </div>
</section>

<!-- Back page -->
<section class="page page--back" aria-label="Why choose us and contact details">
  <div class="abs back__dark"></div>
  <div class="photo back__photo" role="img" aria-label="Photo of an apartment dining area with table lamp and yellow chairs"></div>

  <div class="brand"><span class="brand__mark"></span><span class="brand__name">BRIGHTWIRE PRO</span></div>

  <h1 class="abs why"><span>WHY</span><br>CHOOSE</h1>
  <div class="abs why__brand">BRIGHTWIRE PRO</div>
  <div class="abs why__rule"></div>

  <div class="feature" style="left:26px;top:200px">
    <div class="feature__head"><span class="feature__icon"><svg width="16" height="16" viewBox="0 0 16 16"><path d="M3 9l4-6 3 2-1 3h4l-2 6H5z" fill="#fff"/></svg></span><span class="feature__label">Support when you<br>need it most</span></div>
    <p class="feature__text">BrightWire Pro provides around the clock assis-tance, whether during normal business hours or emergencies we are focused on providing solutions for our clients.</p>
  </div>
  <div class="feature" style="left:232px;top:200px">
    <div class="feature__head"><span class="feature__icon"><svg width="16" height="16" viewBox="0 0 16 16"><circle cx="8" cy="5" r="2.3" fill="#fff"/><circle cx="3.5" cy="6" r="1.7" fill="#fff"/><circle cx="12.5" cy="6" r="1.7" fill="#fff"/><path d="M4 13a4 4 0 0 1 8 0zM0.5 12a3 3 0 0 1 4-2.5L4 12zM15.5 12a3 3 0 0 0-4-2.5L12 12z" fill="#fff"/></svg></span><span class="feature__label">Fast &amp; responsive team<br>with a direct contact</span></div>
    <p class="feature__text">BrightWire Pro treats every one of our clients as a VIP. We pride ourselves on being able to pro-vide a quick turn around for all our jobs. We make the whole process smooth, from book-ing the job to attending and completion.</p>
  </div>
  <div class="feature" style="left:26px;top:306px">
    <div class="feature__head"><span class="feature__icon"><svg width="16" height="16" viewBox="0 0 16 16"><circle cx="7" cy="6" r="2.4" fill="#fff"/><path d="M2.5 13a4.5 4.5 0 0 1 9 0z" fill="#fff"/><circle cx="12.5" cy="11.5" r="2.5" fill="#fff"/><path d="M11.3 11.5l.9.9 1.6-1.7" stroke="#e8261e" stroke-width="1" fill="none"/><path d="M3 2.5l.5 1 1 .2-.8.7.2 1-.9-.5-.9.5.2-1-.8-.7 1-.2z" fill="#fff"/></svg></span><span class="feature__label">Satisfaction with<br>loyalty and integrity</span></div>
    <p class="feature__text">We value our transparency and communica-tion skills to deliver an outstanding perfor-mance which reflects our happy customer base.</p>
  </div>
  <div class="feature" style="left:232px;top:306px">
    <div class="feature__head"><span class="feature__icon"><svg width="16" height="16" viewBox="0 0 16 16"><circle cx="8" cy="6" r="3" fill="#fff"/><path d="M3 14a5 5 0 0 1 10 0z" fill="#fff"/><path d="M4.5 6a3.5 3.5 0 0 1 7 0" stroke="#fff" stroke-width="1.2" fill="none"/></svg></span><span class="feature__label">We provide<br>courtesy calls</span></div>
    <p class="feature__text">The appointment will be confirmed the day before and our technicians will call you half an hour in advance on approach to the job</p>
  </div>
  <div class="feature" style="left:232px;top:398px">
    <div class="feature__head"><span class="feature__icon"><svg width="16" height="16" viewBox="0 0 16 16"><path d="M4 6a4 4 0 0 1 8 0z" fill="#fff"/><rect x="3" y="6" width="10" height="1.4" fill="#fff"/><circle cx="8" cy="9.5" r="2" fill="#fff"/><circle cx="12" cy="13" r="2.2" fill="none" stroke="#fff" stroke-width="1.3"/><path d="M2 14l4-4" stroke="#fff" stroke-width="1.5"/></svg></span><span class="feature__label">Licensed and<br>insured technicians</span></div>
    <p class="feature__text" style="margin-top:12px">All our technicians are experts of their field, with the relevant equipment, knowledge and licenses to carry out our duties.</p>
  </div>

  <h2 class="abs contact-title"><span>CONTACT</span><br>AND LICENSES</h2>
  <div class="abs contact-rule"></div>

  <div class="person" style="left:26px">
    <div class="person__name person__name--red">DANIEL</div>
    <div class="pill pill--ink"><span class="pill__dot"><svg width="6" height="6" viewBox="0 0 10 10"><path d="M2 1l2 2-1 1.5a6 6 0 0 0 2.5 2.5L7 6l2 2-1.5 1.5C4 9 1 6 .5 2.5z" fill="#e8261e"/></svg></span>0412 580 736</div>
  </div>
  <div class="person" style="left:118px">
    <div class="person__name">MARCUS</div>
    <div class="pill pill--red"><span class="pill__dot"><svg width="6" height="6" viewBox="0 0 10 10"><path d="M2 1l2 2-1 1.5a6 6 0 0 0 2.5 2.5L7 6l2 2-1.5 1.5C4 9 1 6 .5 2.5z" fill="#151515"/></svg></span>0438 216 904</div>
  </div>

  <p class="abs lic"><span>ELECTRICAL LICENSE NUMBER</span>BRIGHTWIRE PRO PTY LTD – 619382C</p>
  <p class="abs liability"><span>PUBLIC LIABILITY</span>$20,000,000</p>

  <div class="badge" style="left:232px"><div class="badge__name">DANIEL</div><div class="badge__num"><i></i>512763C</div></div>
  <div class="badge" style="left:318px"><div class="badge__name">MARCUS</div><div class="badge__num"><i></i>278104C</div></div>
  <p class="abs abn">ABN: 5813 2047 916</p>

  <div class="abs email"><svg width="10" height="10" viewBox="0 0 10 10" aria-hidden="true"><path d="M10 0L0 4.5l3.5 1.3L4.5 10 6 6.5z" fill="#e8261e"/></svg>services@brightwirepro.com.au</div>
  <div class="abs back__foot"></div>
</section>

</body>
</html>
```